Lantern Holdings Business Card

We are looking to design new business cards for our company. We have two office locations and would like to have both full addresses on the card. Each address needs two lines for the building name and street address and a line or two for the city, state and zip code. There should be a place for 2-3 phone numbers. The addresses and phone numbers are at the bottom of this description. We also need a place to put our company website and one email address. Our logo is attached.
We would like the card to be two sided. The back of the card should have a blue background with some part of our logo design on it. We would like the full logo on the front of the card as well. The front of the card should have a white background with the blue logo. We are open to listing our addresses on the front or the back of the card. The person who designed our logo gave us an excellent business card idea that we really liked. I have attached a picture of his business card idea so that we can build off of it.
Addresses:
The Marlow Exchange
2214 47th Street NW
Washington, DC 20419
Osprey Harbor Tower
815 Tamsin Boulevard #2207
Miami, FL 33987
Phone Numbers: (202) 555-0148
(202) 555-0193
Website: www.lanternholdings-example.com

```html
<!DOCTYPE html>
<html lang="en">
<head>
<meta charset="utf-8">
<title>Lantern Holdings Business Card</title>
<link rel="stylesheet" href="https://fonts.googleapis.com/css2?family=Lato:wght@400;700&display=swap">
<style>
  :root {
    --stage: #ece9e4;
    --card-white: #ffffff;
    --card-white-shade: #eeeeee;
    --brand-navy: #1f3a94;
    --back-top: #2a56c9;
    --back-bottom: #1d3690;
    --mark-tile: #3a6ed8;
    --text-light: #ffffff;
    --rule: rgba(255,255,255,0.75);
  }
  html, body {
    margin: 0;
    padding: 0;
    width: 1200px;
    height: 1000px;
    overflow: hidden;
    background: var(--stage);
    font-family: "Lato", sans-serif;
  }
  .stage {
    position: relative;
    width: 1200px;
    height: 1000px;
  }
  .card {
    position: absolute;
    top: 270px;
    width: 460px;
    height: 460px;
    border-radius: 36px;
    box-shadow: 0 6px 18px rgba(0,0,0,0.18);
    box-sizing: border-box;
    overflow: hidden;
  }
  .card--front {
    left: 110px;
    background: linear-gradient(160deg, var(--card-white-shade) 0%, var(--card-white) 55%);
  }
  .card--back {
    left: 630px;
    padding-top: 34px;
    background: linear-gradient(180deg, var(--back-top) 0%, var(--back-bottom) 100%);
    color: var(--text-light);
    text-align: center;
  }
  .wordmark {
    position: absolute;
    left: 36px;
    bottom: 64px;
    display: flex;
    align-items: center;
    gap: 12px;
  }
  .wordmark__square {
    width: 46px;
    height: 46px;
    border-radius: 8px;
    background: var(--brand-navy);
  }
  .wordmark__name {
    font-size: 28px;
    font-weight: 400;
    letter-spacing: 1px;
    color: var(--brand-navy);
    text-transform: uppercase;
  }
  .back-mark {
    width: 130px;
    height: 130px;
    margin: 0 auto;
    border-radius: 16px;
    background: var(--mark-tile);
  }
  .back-name {
    margin-top: 10px;
    font-size: 15px;
    line-height: 18px;
    letter-spacing: 1px;
    text-transform: uppercase;
  }
  .office {
    margin: 12px auto 0;
    font-size: 16px;
    line-height: 20px;
  }
  .rule {
    width: 250px;
    margin: 10px auto 0;
    border-top: 1px dashed var(--rule);
  }
  .phones {
    margin-top: 10px;
    font-size: 15px;
    line-height: 18px;
  }
  .contact {
    margin-top: 8px;
    font-size: 14px;
    line-height: 18px;
  }
</style>
</head>
<body>
<main class="stage">
  <section class="card card--front" aria-label="Card front">
    <div class="wordmark">
      <span class="wordmark__square"></span>
      <span class="wordmark__name">Lantern Holdings</span>
    </div>
  </section>

  <section class="card card--back" aria-label="Card back">
    <div class="back-mark"></div>
    <div class="back-name">Lantern Holdings</div>
    <div class="office">
      The Marlow Exchange<br>
      2214 47th Street NW<br>
      Washington, DC 20419
    </div>
    <div class="rule"></div>
    <div class="office">
      Osprey Harbor Tower<br>
      815 Tamsin Boulevard #2207<br>
      Miami, FL 33987
    </div>
    <div class="rule"></div>
    <div class="phones">(202) 555-0148 | (202) 555-0193</div>
    <div class="contact">
      www.lanternholdings-example.com<br>
      info@lanternholdings-example.com
    </div>
  </section>
</main>
</body>
</html>
```